Advertisement Design

I'm looking for a post card sized advertisement piece that I will be dropping off to commercial and residential customers.
On one side I want it promoting carpet cleaning services and on the other side dryer vent cleaning services.
I've uploaded two different layouts of my company logo for you to choice from.
One batch will be printed with my Michigan Number
One batch will be printed with my Tennessee number
Will share contact numbers with the winner so just use a make up number
555-319-4826

Slow in providing feedback

```html
<!DOCTYPE html>
<html lang="en">
<head>
<meta charset="utf-8">
<title>Loom Lane Postcards</title>
<link href="https://fonts.googleapis.com/css2?family=Montserrat:wght@400;600;700;800&display=swap" rel="stylesheet">
<style>
  :root {
    --page: #ffffff;
    --charcoal: #1c1c1c;
    --brand-blue: #0a7bbf;
    --slate: #545659;
    --white: #ffffff;
    --ink: #2b2b2b;
  }
  * { box-sizing: border-box; margin: 0; padding: 0; }
  html, body { width: 1200px; height: 1200px; overflow: hidden; background: var(--page); }
  body { position: relative; font-family: "Montserrat", Arial, sans-serif; }

  .postcard {
    position: absolute;
    width: 796px;
    height: 564px;
    overflow: hidden;
  }
  .postcard--carpet { left: 62px; top: 48px; background: var(--charcoal); }
  .postcard--dryer { left: 342px; top: 588px; background: var(--brand-blue); }

  .postcard__photo {
    position: absolute;
    left: 497px; top: 0;
    width: 299px; height: 564px;
  }
  .postcard--carpet .postcard__photo {
    background: linear-gradient(180deg, #e9e6e1 0%, #d8d2ca 50%, #b9aea2 75%, #cfc5b9 100%);
  }
  .postcard--dryer .postcard__photo {
    background: linear-gradient(160deg, #a9a9a9 0%, #7d7d7d 35%, #3b3b3b 60%, #bfc1c4 80%, #6e6e6e 100%);
  }

  .postcard__copy {
    position: absolute;
    left: 0; top: 0;
    width: 497px;
    text-align: center;
    color: var(--white);
  }
  .postcard__eyebrow {
    margin-top: 34px;
    font-weight: 700;
    font-size: 17px;
    letter-spacing: 0.2px;
  }
  .postcard__headline {
    margin-top: 4px;
    font-weight: 800;
    font-size: 66px;
    line-height: 68px;
    letter-spacing: -0.5px;
  }
  .postcard__region {
    margin-top: 6px;
    font-weight: 700;
    font-size: 17px;
  }

  .brand {
    position: absolute;
    left: 78px; top: 326px;
    height: 98px;
    display: flex;
    align-items: center;
    color: var(--white);
  }
  .brand__square {
    width: 68px; height: 68px;
    border-radius: 8px;
    background: var(--white);
    opacity: 1;
  }
  .postcard--carpet .brand__square { background: var(--brand-blue); border: 3px solid var(--white); }
  .brand__divider {
    width: 4px; height: 98px;
    background: var(--white);
    margin: 0 18px 0 20px;
  }
  .brand__name {
    font-weight: 600;
    font-size: 25px;
    line-height: 28px;
    text-align: left;
    letter-spacing: 0.5px;
  }

  .contact-bar {
    position: absolute;
    left: 25px; top: 465px;
    width: 746px; height: 65px;
    border-radius: 10px;
    overflow: hidden;
    display: flex;
  }
  .contact-bar__phone {
    width: 472px;
    display: flex; align-items: center; justify-content: center;
    color: var(--white);
    font-weight: 400;
    font-size: 48px;
    letter-spacing: 0.5px;
  }
  .postcard--carpet .contact-bar__phone { background: var(--brand-blue); }
  .postcard--dryer .contact-bar__phone { background: var(--slate); }
  .contact-bar__web {
    flex: 1;
    background: var(--white);
    display: flex; align-items: center;
    color: var(--ink);
    font-weight: 600;
    font-size: 28px;
    letter-spacing: 1.5px;
  }
  .contact-bar__icon { width: 36px; height: 36px; margin: 0 8px 0 -16px; }
</style>
</head>
<body>

<section class="postcard postcard--carpet">
  <div class="postcard__photo" role="img" aria-label="Technician cleaning a beige carpet with an extraction wand in a living room"></div>
  <div class="postcard__copy">
    <p class="postcard__eyebrow">RESIDENTIAL AND COMMERCIAL</p>
    <h1 class="postcard__headline">CARPET<br>CLEANING<br>SERVICES</h1>
    <p class="postcard__region">and more in Michigan &amp; Tennessee</p>
  </div>
  <div class="brand">
    <div class="brand__square"></div>
    <div class="brand__divider"></div>
    <div class="brand__name">LOOM LANE<br>PROPERTY SERVICES</div>
  </div>
  <div class="contact-bar">
    <div class="contact-bar__phone">555-319-4826</div>
    <div class="contact-bar__web">
      <svg class="contact-bar__icon" viewBox="0 0 36 36" aria-hidden="true">
        <circle cx="18" cy="18" r="16" fill="#ffffff" stroke="#0a7bbf" stroke-width="3"/>
        <path d="M25 11 L11 17 L17 19 L19 25 Z" fill="#2b2b2b"/>
      </svg>
      loomlane.com
    </div>
  </div>
</section>

<section class="postcard postcard--dryer">
  <div class="postcard__photo" role="img" aria-label="Vacuum hose cleaning out a foil dryer vent duct"></div>
  <div class="postcard__copy">
    <p class="postcard__eyebrow" style="margin-top:30px">RESIDENTIAL AND COMMERCIAL</p>
    <h1 class="postcard__headline">DRYER VENT<br>CLEANING<br>SERVICES</h1>
    <p class="postcard__region">and more in Michigan &amp; Tennessee</p>
  </div>
  <div class="brand">
    <div class="brand__square"></div>
    <div class="brand__divider"></div>
    <div class="brand__name">LOOM LANE<br>PROPERTY SERVICES</div>
  </div>
  <div class="contact-bar">
    <div class="contact-bar__phone">555-319-4826</div>
    <div class="contact-bar__web">
      <svg class="contact-bar__icon" viewBox="0 0 36 36" aria-hidden="true">
        <circle cx="18" cy="18" r="16" fill="#0a7bbf"/>
        <path d="M25 11 L11 17 L17 19 L19 25 Z" fill="#ffffff"/>
      </svg>
      loomlane.com
    </div>
  </div>
</section>

</body>
</html>
```